Flyer design that will be used as a landing page for a penny auctions website

We are a new company named ZolvaTap where users can bid on auctions for just pennies and win items at up to 98% off retail value. I would like for it to be bubbly and eye-catching, similar to the design of my logo. I would like for it to include the following features:

1) Logo and/or just the name "ZolvaTap" in any place applicable.
2) Show products such as electronics (tv, gamrix, vidoconsole, etc.) that can be won at 98% off retail price.
3) Content showcasing that our products are always brand new, include fast shipping and better than competing auction sites such as marko, without distinctly having any of their logos on the page.
4) Registration buttons in multiple places for maximum exposure.
5) How it works section: Register an account, purchase the starter package, start bidding and save up to 98% off.
7) The most important part will be a registration area at the top of the flyer which will ask users to signup, most include text area's for First Name, Last Name, Email Address, Confirm Email, Username, Password, Confirm Password, and Promo Code.

This flyer will be on my website and needs to be roughly 960px wide. I will be adding input elements such as textbox's and links/buttons to the flyer once I get it onto the site so it needs to be ready to immediately publish upon completion.

Here are some links below to show how the competition has their flyers setup, they are vary well done and I would like to have one that is similar but different:
- https://www.fernolots.com/en/landing/
- https://register.sunnylotmart.com/register-revshare20.php

```html
<!DOCTYPE html>
<html lang="en">
<head>
<meta charset="utf-8">
<title>ZolvaTap – Win items at 98% off</title>
<link rel="stylesheet" href="https://fonts.googleapis.com/css2?family=Open+Sans:ital,wght@0,400;0,600;0,700;1,400&display=swap">
<style>
  :root{
    --black:#000;
    --white:#fff;
    --sky:#6dc9f4;
    --sun:#f4de6c;
    --mint:#6ef282;
    --coral:#f4876d;
    --ink:#222;
    --label:#555;
    --field:#b9b9b9;
    --price-blue:#1f5f86;
    --price-olive:#8a7a12;
    --price-green:#167a2a;
    --price-red:#8e2614;
    --social:#5bc3ee;
  }
  *{box-sizing:border-box;margin:0;padding:0}
  html,body{width:1200px;height:2474px;overflow:hidden;background:var(--white)}
  body{position:relative;font-family:"Open Sans",Arial,sans-serif;color:var(--ink)}
  .abs{position:absolute}

  .top-bar{left:0;top:0;width:1200px;height:115px;background:var(--black)}
  .register-top{left:903px;top:0;width:297px;height:91px;background:var(--coral);border-radius:0 0 0 46px 0;border-bottom-left-radius:46px;border-top-left-radius:46px;color:var(--white);font-size:38px;display:flex;align-items:center;justify-content:center;letter-spacing:1px}

  .brand{left:0;top:0;width:330px;height:330px;background:var(--black);border-bottom-right-radius:150px;display:flex;flex-direction:column;align-items:center;justify-content:center;gap:18px;padding-right:30px}
  .brand-mark{width:62px;height:62px;background:var(--sun);border-radius:10px}
  .brand-name{font-size:44px;font-weight:700;color:var(--sun)}

  .pill{border-radius:190px}
  .pill-phone{left:41px;top:371px;width:615px;height:363px;background:var(--sky)}
  .pill-desktop{left:680px;top:177px;width:363px;height:627px;background:var(--sun)}
  .pill-console{left:435px;top:470px;width:365px;height:555px;background:var(--mint)}
  .pill-tv{left:542px;top:903px;width:627px;height:363px;background:var(--coral)}

  .product{border-radius:14px}
  .product-phone{left:134px;top:410px;width:320px;height:270px;background:linear-gradient(135deg,#2f4f6a,#10202e);transform:rotate(-28deg);border-radius:30px}
  .product-desktop{left:712px;top:258px;width:300px;height:238px;background:linear-gradient(160deg,#c75a2a,#3a1a14 70%,#c9c9c9)}
  .product-console{left:495px;top:536px;width:216px;height:248px;background:linear-gradient(180deg,#1b1b1b,#050505);border-radius:8px}
  .product-tv{left:635px;top:996px;width:298px;height:196px;background:linear-gradient(180deg,#c98a7a,#6a6a6a 55%,#2a2a2a)}

  .price{width:110px;height:110px;border-radius:50%;background:var(--white);display:flex;flex-direction:column;align-items:center;justify-content:center;line-height:1.1}
  .price small{font-size:21px;font-weight:600;color:#333}
  .price b{font-size:34px;font-weight:700}
  .price-phone{left:112px;top:430px}
  .price-phone b{color:var(--price-blue)}
  .price-desktop{left:862px;top:556px}
  .price-desktop b{color:var(--price-olive)}
  .price-console{left:467px;top:852px}
  .price-console b{color:var(--price-green)}
  .price-tv{left:980px;top:982px}
  .price-tv b{color:var(--price-red)}

  .promo{left:52px;top:825px;width:284px;height:346px;background:var(--sun);display:flex;flex-direction:column;align-items:center;justify-content:center;text-align:center;font-size:34px;line-height:1.3;color:var(--black)}
  .promo .accent{color:var(--coral);font-size:42px}
  .promo .tight{font-size:30px}

  .signup{left:52px;top:1371px;width:455px}
  .field{height:90px}
  .field label{display:block;font-size:26px;color:var(--label);margin-left:4px;line-height:30px}
  .field .input{height:38px;border:2px solid var(--field);border-top-width:3px;background:var(--white)}

  .submit{left:0;top:2140px;width:501px;height:97px;background:var(--coral);border-radius:0 50px 50px 0;color:var(--white);font-size:36px;display:flex;align-items:center;padding-left:30px;letter-spacing:1px}

  .steps{left:571px;top:1359px;width:590px;height:517px;background:var(--sun)}
  .steps-rail{left:652px;top:1402px;width:146px;height:433px;background:var(--black);border-radius:73px}
  .step-icon{width:80px;height:80px}
  .step-text{left:831px;font-size:31px;font-style:italic;color:var(--black);line-height:1.15}

  .perks{left:715px;top:1876px;width:446px;height:404px;background:var(--mint)}
  .perks-rail{left:969px;top:1913px;width:124px;height:334px;background:var(--black);border-radius:62px}
  .perk-text{right:256px;font-size:24px;font-style:italic;color:var(--black);text-align:right;line-height:1.2}
  .perk-badge{left:995px;width:72px;height:72px}
  .marko{left:981px;top:2163px;width:100px;text-align:center;font-size:28px;font-weight:700;color:var(--sun)}

  .footer{left:0;top:2350px;width:1200px;height:124px;background:var(--black)}
  .footer-text{left:604px;top:2423px;font-size:24px;color:var(--white)}
  .social{width:70px;height:70px;border-radius:50%;background:var(--social);color:var(--white);font-size:13px;font-weight:700;display:flex;align-items:center;justify-content:center;top:2375px}
</style>
</head>
<body>
  <div class="abs top-bar"></div>
  <div class="abs register-top">REGISTER</div>

  <div class="abs brand">
    <div class="brand-mark"></div>
    <div class="brand-name">ZolvaTap</div>
  </div>

  <div class="abs pill pill-phone"></div>
  <div class="abs pill pill-desktop"></div>
  <div class="abs pill pill-console"></div>
  <div class="abs pill pill-tv"></div>

  <div class="abs product product-phone" role="img" aria-label="Korvana smartphone"></div>
  <div class="abs product product-desktop" role="img" aria-label="All-in-one desktop computer with keyboard"></div>
  <div class="abs product product-console" role="img" aria-label="gamrix game console with motion sensor"></div>
  <div class="abs product product-tv" role="img" aria-label="Flat screen television showing a mountain lake"></div>

  <div class="abs price price-phone"><small>sold for</small><b>15$</b></div>
  <div class="abs price price-desktop"><small>sold for</small><b>15$</b></div>
  <div class="abs price price-console"><small>sold for</small><b>15$</b></div>
  <div class="abs price price-tv"><small>sold for</small><b>15$</b></div>

  <div class="abs promo">
    <span>WIN ITEMS</span>
    <span>AT</span>
    <span class="accent">98% OFF</span>
    <span>OF THEIR</span>
    <span class="tight">RETAIL PRICE!</span>
  </div>

  <div class="abs signup">
    <div class="field"><label>First Name</label><div class="input"></div></div>
    <div class="field"><label>Last Name</label><div class="input"></div></div>
    <div class="field"><label>Email Address</label><div class="input"></div></div>
    <div class="field"><label>Confirm Email</label><div class="input"></div></div>
    <div class="field"><label>Username</label><div class="input"></div></div>
    <div class="field"><label>Password</label><div class="input"></div></div>
    <div class="field"><label>Confirm Password</label><div class="input"></div></div>
    <div class="field"><label>Promo Code</label><div class="input"></div></div>
  </div>

  <div class="abs submit">SUBMIT AND REGISTER</div>

  <div class="abs steps"></div>
  <div class="abs steps-rail"></div>

  <svg class="abs step-icon" style="left:685px;top:1436px" viewBox="0 0 80 80" fill="none" stroke="var(--mint)" stroke-width="5">
    <path d="M12 6h34l14 14v54H12z"/><path d="M20 24h20M20 36h16M20 48h12"/>
    <circle cx="56" cy="46" r="8" fill="var(--mint)"/><path d="M42 72c2-10 8-14 14-14s12 4 14 14z" fill="var(--mint)"/>
  </svg>
  <svg class="abs step-icon" style="left:685px;top:1578px" viewBox="0 0 80 80" fill="none" stroke="var(--coral)" stroke-width="5" stroke-linecap="round">
    <path d="M6 14h10l8 38h40l8-28H22"/><path d="M44 10v22M36 24l8 8 8-8"/>
    <circle cx="30" cy="64" r="5" fill="var(--coral)"/><circle cx="58" cy="64" r="5" fill="var(--coral)"/>
  </svg>
  <svg class="abs step-icon" style="left:685px;top:1722px" viewBox="0 0 80 80" fill="var(--sky)">
    <rect x="30" y="8" width="24" height="14" rx="3" transform="rotate(45 42 15)"/>
    <rect x="20" y="30" width="24" height="14" rx="3" transform="rotate(45 32 37)"/>
    <rect x="30" y="22" width="16" height="12" transform="rotate(45 38 28)"/>
    <rect x="42" y="36" width="8" height="36" transform="rotate(-45 46 54)"/>
    <rect x="6" y="66" width="40" height="8" rx="3"/>
  </svg>

  <div class="abs step-text" style="top:1456px">register an account</div>
  <div class="abs step-text" style="top:1578px">purchase the<br>starter package</div>
  <div class="abs step-text" style="top:1722px">start bidding and<br>save up to 98% off</div>

  <div class="abs perks"></div>
  <div class="abs perks-rail"></div>

  <svg class="abs perk-badge" style="top:1932px" viewBox="0 0 72 72" fill="var(--sun)">
    <rect x="4" y="18" width="38" height="30" rx="3"/>
    <path d="M44 28h14l10 12v8H44z"/>
    <circle cx="18" cy="54" r="7"/><circle cx="56" cy="54" r="7"/>
    <rect x="0" y="24" width="14" height="4" fill="var(--black)"/><rect x="0" y="34" width="10" height="4" fill="var(--black)"/>
  </svg>
  <svg class="abs perk-badge" style="top:2042px" viewBox="0 0 72 72">
    <circle cx="36" cy="36" r="32" fill="none" stroke="var(--sky)" stroke-width="4" stroke-dasharray="5 4"/>
    <circle cx="36" cy="36" r="24" fill="none" stroke="var(--sky)" stroke-width="2"/>
    <text x="36" y="42" text-anchor="middle" font-family="Open Sans, sans-serif" font-size="15" font-weight="700" fill="var(--sky)" transform="rotate(-15 36 36)">NEW!</text>
  </svg>
  <div class="abs marko">marko</div>

  <div class="abs perk-text" style="top:1955px">fast delivery</div>
  <div class="abs perk-text" style="top:2063px">brand new items</div>
  <div class="abs perk-text" style="top:2158px">better than other<br>auction sites</div>

  <div class="abs footer"></div>
  <div class="abs footer-text">share our deals with your friends</div>
  <div class="abs social" style="left:996px">Facetome</div>
  <div class="abs social" style="left:1091px">Chirpr</div>
</body>
</html>
```